'Vessel types, Demand, Supply & Disruptions - what's currently driving the bulk shipping

This is required for a talk that needs to cover the following matters

the difference between small, handysize, handymax, panamax, capesize, and very large bulk carriers, how the trade differs, self loading/unloading etc as an intro to the dry bulk trade and what's currently driving the bulk shipping markets.

The below is an initial breakdown on the slides but not finalised

There will need to be an additional slide on the importance of China for the dry bulk trades

Slide 1: Introduction

Welcome and brief overview of dry bulk shipping
Importance in global trade and economy
Slide 2: Types of Dry Bulk Vessels

Capesize: 100,000-400,000 DWT
Panamax: 60,000-100,000 DWT
Supramax: 45,000-60,000 DWT
Handysize: 15,000-45,000 DWT
Description and key features of each vessel type
Slide 3: Vessel Characteristics

Holds and hatches
Draft, beam, and length
Cargo handling equipment
Engine types and power
Slide 4: Routing in Dry Bulk Shipping

Major shipping routes (e.g., Cape of Good Hope, Panama Canal)
Factors influencing routing decisions (e.g., weather, fuel costs)
Strategic chokepoints and canals
Slide 5: Fixing and Chartering

Voyage Charter
Owner's responsibility
Charterer's responsibility
Time Charter
Bareboat Charter
Spot and long-term contracts
Slide 6: Key Charter Party (CP) Terms

Laytime and demurrage
Freight rates
Notice of Readiness (NOR)
Cargo quantities and quality
Ballast bonus
Slide 7: Current Disruptions in Dry Bulk Shipping

Impact of geopolitical events (e.g., trade tensions, conflicts) on shipping lanes
Effects of economic downturns (e.g., COVID-19 pandemic) on demand and supply chains
Environmental regulations affecting vessel operations
Port congestion and delays
Slide 8: Market Trends and Innovations

Technological advancements in vessel design (e.g., eco-friendly propulsion systems, fuel efficiency)
Digitalization and smart shipping solutions
Sustainability initiatives in the industry (e.g., ballast water treatment, emissions reduction)
Slide 9: Mitigation Strategies for Disruptions

Diversification of trading routes and markets
Investment in fleet optimization and efficiency measures
Collaboration with industry partners and stakeholders to address common challenges
Continuous monitoring and adaptation to changing market conditions
Slide 10: Case Study

Example of a recent disruption and its impact on dry bulk shipping operations
Lessons learned and strategies employed to mitigate the effects
Slide 11: Future Outlook

Anticipated trends and challenges in the dry bulk shipping industry
Opportunities for innovation and growth
Importance of sustainability and resilience in shaping the future of the industry
Slide 12: Conclusion

Recap of key points
Call to action for stakeholders to collaborate and innovate for a sustainable and resilient dry bulk shipping industry
Slide 13: Q&A

```html
<!DOCTYPE html>
<html lang="en">
<head>
<meta charset="utf-8">
<title>Dry Bulk Talk – Trade and Market Drivers</title>
<link rel="stylesheet" href="https://fonts.googleapis.com/css2?family=Poppins:wght@300;400;500;600&display=swap">
<style>
  :root {
    --canvas: #c8c8c8;
    --paper: #ffffff;
    --navy: #0a6fc2;
    --brand: #0f6fc1;
    --sky: #2ea6ec;
    --cyan: #00aeef;
    --ink: #111111;
    --grey-text: #555555;
    --note-bg: #efefef;
    --note-text: #8a8a8a;
    --ore: #23a8ee;
    --ore-cape: #00aeef;
    --coal: #1d5e93;
    --grain: #72b2e3;
    --minor: #a7d0f1;
    --bauxite: #d3e7f7;
  }
  * { box-sizing: border-box; margin: 0; padding: 0; }
  html, body { width: 1068px; height: 1200px; overflow: hidden; }
  body { background: var(--canvas); font-family: "Poppins", sans-serif; position: relative; }

  .slide { position: absolute; left: 85px; width: 899px; height: 506px; background: var(--paper);
           box-shadow: 0 14px 26px rgba(0,0,0,.22); overflow: hidden; }
  .slide--trade { top: 81px; }
  .slide--drivers { top: 630px; }
  .abs { position: absolute; }

  /* Slide 1 */
  .side-stripe { left: 0; top: 0; width: 19px; height: 100%; background: var(--brand); }
  .trade-title { left: 45px; top: 43px; font-size: 36px; font-weight: 600; line-height: 34px; color: var(--brand); letter-spacing: .2px; }
  .trade-title .year { color: var(--sky); display: block; }
  .trade-subtitle { left: 45px; top: 122px; font-size: 18px; font-weight: 500; color: var(--ink); }
  .fact { left: 62px; color: var(--grey-text); font-size: 15px; line-height: 20px; font-weight: 400; }
  .fact .hl { color: var(--sky); }
  .fact .lead { font-size: 19px; color: #333; line-height: 24px; }
  .chev { position: absolute; left: -14px; color: var(--sky); font-size: 15px; font-weight: 500; }
  .fact--volume { top: 151px; }
  .fact--tonne { top: 199px; }
  .fact--bulk { top: 259px; line-height: 18.5px; }
  .fact--bulk .lead { display: block; margin-bottom: 3px; }

  .classes-box { left: 41px; top: 349px; width: 253px; height: 132px; background: var(--cyan); border-radius: 8px; color: #fff; }
  .classes-box .lead { position: absolute; left: 24px; top: 12px; font-size: 17px; line-height: 20px; font-weight: 400; }
  .classes-box .cls { position: absolute; font-size: 16px; font-weight: 400; }
  .classes-box .cls::before { content: "›"; position: absolute; left: -16px; top: -1px; font-size: 19px; }

  .cargo-chart { left: 403px; top: 25px; width: 470px; height: 470px; }

  /* Slide 2 */
  .drivers-title { left: 45px; top: 28px; font-size: 34px; font-weight: 600; color: var(--sky); letter-spacing: .3px; }
  .driver-box { left: 41px; width: 324px; border-radius: 4px; color: #fff; }
  .driver-box--demand { top: 87px; height: 172px; background: #33a6ec; }
  .driver-box--supply { top: 285px; height: 182px; background: var(--navy); }
  .driver-box h3 { position: absolute; left: 17px; top: 10px; font-size: 17.5px; font-weight: 600; }
  .driver-box p { position: absolute; left: 18px; font-size: 14px; line-height: 16px; font-weight: 400; width: 300px; }
  .wave { position: absolute; right: 0; top: 0; width: 96px; height: 26px;
          background: linear-gradient(90deg, rgba(255,255,255,0) 0%, rgba(230,246,255,.85) 100%);
          border-radius: 0 4px 0 26px; }

  .disruptions-panel { left: 550px; top: 0; width: 349px; height: 100%; background: var(--sky); color: #fff; }
  .disruptions-panel h2 { position: absolute; left: 18px; top: 38px; font-size: 23px; font-weight: 500; }
  .disruption { position: absolute; left: 38px; font-size: 19px; line-height: 21px; font-weight: 400; }
  .disruption::before { content: "›"; position: absolute; left: -20px; top: 0; font-size: 20px; }
  .disruption strong { font-weight: 600; display: block; margin-bottom: 5px; }
</style>
</head>
<body>

<section class="slide slide--trade">
  <div class="abs side-stripe"></div>
  <h1 class="abs trade-title">Total World Trade <span class="year">2022</span></h1>
  <div class="abs trade-subtitle">Oil, Bulk, Containers, Gas &amp; Others</div>

  <div class="abs fact fact--volume"><span class="chev">›</span>Approx. <span class="hl">12 billion</span> mts &amp;<br><span class="hl">58.4</span> billion tonne-miles</div>
  <div class="abs fact fact--tonne"><span class="chev" style="top:3px">›</span><span class="lead">Tonne Mile</span><br>Cargo Weight x Distance Carried</div>
  <div class="abs fact fact--bulk"><span class="chev" style="top:3px">›</span><span class="lead">Dry Bulk</span><span class="hl">5.3</span> Billion mts / <span class="hl">44%</span> of Total<br>But <span class="hl">9%</span> of Tonne Miles</div>

  <div class="abs classes-box">
    <div class="lead">Majority carried on 4<br>classes of vessels</div>
    <span class="cls" style="left:41px;top:58px">Capesize</span>
    <span class="cls" style="left:149px;top:59px">Supramax</span>
    <span class="cls" style="left:41px;top:85px">Panamax</span>
    <span class="cls" style="left:149px;top:86px">Handysize</span>
  </div>

  <svg class="abs cargo-chart" viewBox="830 180 800 800" role="img" aria-label="Stacked bar chart of cargo share per vessel segment, 2022">
    <g font-family="Poppins, sans-serif">
      <rect x="1173" y="191" width="430" height="173" rx="14" fill="var(--note-bg)"/>
      <g font-size="19" fill="var(--note-text)" font-weight="300">
        <text x="1196" y="229">*Minor Bulks = Fertilisers, Steel,</text>
        <text x="1196" y="257">Bagged/Bulky grain cargoes (rice,</text>
        <text x="1196" y="284">sugar, etc) Cement, Petroleum coke,</text>
        <text x="1196" y="312">Scrap, Forest Products, Minerals, Salts,</text>
        <text x="1196" y="339">Aggregates, Minor raw materials</text>
      </g>

      <g>
        <rect x="848" y="625" width="27" height="28" fill="var(--bauxite)"/>
        <rect x="848" y="659" width="27" height="28" fill="var(--minor)"/>
        <rect x="848" y="693" width="27" height="28" fill="var(--grain)"/>
        <rect x="848" y="727" width="27" height="28" fill="var(--coal)"/>
        <rect x="848" y="761" width="27" height="28" fill="var(--ore)"/>
      </g>
      <g font-size="16" fill="#666">
        <text x="882" y="648">Bauxite</text>
        <text x="882" y="682">Minor</text>
        <text x="882" y="716">Grains</text>
        <text x="882" y="750">Coal</text>
        <text x="882" y="783">Iron Ore</text>
      </g>
      <g font-size="19" fill="#111">
        <text x="845" y="821">Community Share</text>
        <text x="845" y="841">Per Segment 2022</text>
        <text x="845" y="861">(DWT * Duration)</text>
      </g>

      <line x1="1039" y1="372" x2="1039" y2="868" stroke="#222" stroke-width="2"/>
      <line x1="1039" y1="868" x2="1605" y2="868" stroke="#222" stroke-width="2"/>

      <!-- Total Dry Bulk -->
      <rect x="1080" y="422" width="84" height="29" fill="var(--bauxite)"/>
      <rect x="1080" y="451" width="84" height="85" fill="var(--minor)"/>
      <rect x="1080" y="536" width="84" height="57" fill="var(--grain)"/>
      <rect x="1080" y="593" width="84" height="120" fill="var(--coal)"/>
      <rect x="1080" y="713" width="84" height="155" fill="var(--ore)"/>
      <!-- Capesize -->
      <rect x="1184" y="420" width="84" height="59" fill="var(--bauxite)"/>
      <rect x="1184" y="479" width="84" height="12" fill="var(--grain)"/>
      <rect x="1184" y="491" width="84" height="83" fill="var(--coal)"/>
      <rect x="1184" y="574" width="84" height="294" fill="var(--ore-cape)"/>
      <!-- Panamax -->
      <rect x="1288" y="420" width="84" height="13" fill="var(--bauxite)"/>
      <rect x="1288" y="433" width="84" height="46" fill="var(--minor)"/>
      <rect x="1288" y="479" width="84" height="141" fill="var(--grain)"/>
      <rect x="1288" y="620" width="84" height="213" fill="var(--coal)"/>
      <rect x="1288" y="833" width="84" height="35" fill="var(--ore-cape)"/>
      <!-- Supramax -->
      <rect x="1391" y="420" width="84" height="10" fill="var(--bauxite)"/>
      <rect x="1391" y="430" width="84" height="237" fill="var(--minor)"/>
      <rect x="1391" y="667" width="84" height="85" fill="var(--grain)"/>
      <rect x="1391" y="752" width="84" height="86" fill="var(--coal)"/>
      <rect x="1391" y="838" width="84" height="30" fill="var(--ore-cape)"/>
      <!-- Handysize -->
      <rect x="1494" y="419" width="84" height="8" fill="var(--bauxite)"/>
      <rect x="1494" y="427" width="84" height="265" fill="var(--minor)"/>
      <rect x="1494" y="692" width="84" height="107" fill="var(--grain)"/>
      <rect x="1494" y="799" width="84" height="54" fill="var(--coal)"/>
      <rect x="1494" y="853" width="84" height="15" fill="var(--ore-cape)"/>

      <g font-size="19" font-weight="600" text-anchor="middle">
        <text x="1122" y="505" fill="#fff">23%</text>
        <text x="1122" y="574" fill="#fff">14%</text>
        <text x="1122" y="669" fill="#fff">24%</text>
        <text x="1122" y="800" fill="#fff">33%</text>
        <text x="1226" y="458" fill="#111">8%</text>
        <text x="1226" y="540" fill="#fff">20%</text>
        <text x="1226" y="734" fill="#fff">70%</text>
        <text x="1330" y="462" fill="#111">10%</text>
        <text x="1330" y="545" fill="#fff">38%</text>
        <text x="1330" y="738" fill="#fff">43%</text>
        <text x="1330" y="859" fill="#fff">6%</text>
        <text x="1433" y="564" fill="#111">60%</text>
        <text x="1433" y="720" fill="#fff">18%</text>
        <text x="1433" y="803" fill="#fff">18%</text>
        <text x="1536" y="597" fill="#111">68%</text>
        <text x="1536" y="754" fill="#fff">24%</text>
        <text x="1536" y="836" fill="#111">6%</text>
      </g>

      <g font-size="16" fill="#777" text-anchor="middle">
        <text transform="translate(1115 930) rotate(-90)">Total</text>
        <text transform="translate(1138 930) rotate(-90)">Dry Bulk</text>
        <text transform="translate(1231 932) rotate(-90)">Capesize</text>
        <text transform="translate(1339 932) rotate(-90)">Panamax</text>
        <text transform="translate(1437 927) rotate(-90)">Supramax</text>
        <text transform="translate(1545 925) rotate(-90)">Hansize</text>
      </g>
    </g>
  </svg>
</section>

<section class="slide slide--drivers">
  <h2 class="abs drivers-title">What Makes Market Moves?</h2>

  <div class="abs driver-box driver-box--demand">
    <div class="wave" role="img" aria-label="Wave splash decoration"></div>
    <h3>Demand Of Ships</h3>
    <p style="top:38px">Economic/Industrial growth &amp; outlook</p>
    <p style="top:63px">Interest Rates or Disposable Income</p>
    <p style="top:89px">Community Prives and Inventory Levels</p>
    <p style="top:117px">Crop shortfall and Imports to calm<br>inflationary pressures</p>
  </div>

  <div class="abs driver-box driver-box--supply">
    <div class="wave" role="img" aria-label="Wave splash decoration"></div>
    <h3>Supply Of Ships</h3>
    <p style="top:38px">Newbuilding programs – can cause<br>surpluses or defecits</p>
    <p style="top:78px">Congestions or Longer Ton Miles</p>
    <p style="top:105px">Slow Speeding</p>
    <p style="top:134px">Environmental Regulations &amp; Emissions –<br>new fuels, new engine types, technology</p>
  </div>

  <div class="abs disruptions-panel">
    <h2>Disruptions</h2>
    <div class="disruption" style="top:99px"><strong>Global Warming</strong>Panama/Plate/Mississippi<br>Unpredictable patterns</div>
    <div class="disruption" style="top:185px">Sanctions</div>
    <div class="disruption" style="top:226px">Ton miles (Coal from Gas)</div>
    <div class="disruption" style="top:266px"><strong>War</strong>Russia/Ukraine – Red Sea</div>
    <div class="disruption" style="top:348px">Epidemics – Covid</div>
    <div class="disruption" style="top:389px">Occasional Human Error<br>mv Long Harbour</div>
  </div>
</section>

</body>
</html>
```